Business Card Design for Real Estate Company

I am looking for a business card design that will catch my client's attention.

Industry/Entity Type

Business

Requirements
Must have
• Please have the following information in the business card design. You can substitute the "Office, Mobile, email, and web" with an icon or some other design you may think will go well with the business card.

Derek Osmund
482 W. Fenwick St., Suite 310
Pasadena, CA 91348
Office: 626.748.1196
Mobile: 626.913.4071
email: Derek@CrestviewPropertyWalk.example
web: www.CrestviewPropertyWalk.example

```html
<!DOCTYPE html>
<html lang="en">
<head>
<meta charset="utf-8">
<title>Crestview Property Walk – Business Card</title>
<link rel="stylesheet" href="https://fonts.googleapis.com/css2?family=Open+Sans:wght@400&family=Arimo:ital,wght@0,400;0,700;1,700&display=swap">
<style>
  :root {
    --bark: #5c4a1e;
    --mist: #e6e7e8;
    --paper: #ffffff;
    --label-grey: #6d6e70;
    --ink-white: #ffffff;
    --seal: #c9b98a;
  }
  html, body {
    margin: 0;
    padding: 0;
    width: 1200px;
    height: 1000px;
    overflow: hidden;
    background: var(--paper);
  }
  .canvas {
    position: relative;
    width: 1200px;
    height: 1000px;
  }
  .side-label {
    position: absolute;
    top: 266px;
    width: 566px;
    text-align: center;
    font-family: "Open Sans", sans-serif;
    font-size: 44px;
    line-height: 54px;
    color: var(--label-grey);
    letter-spacing: 1px;
  }
  .side-label--front { left: 18px; }
  .side-label--back { left: 619px; }

  .card {
    position: absolute;
    top: 328px;
    width: 566px;
    height: 345px;
    border-radius: 24px;
    background: var(--bark);
    overflow: hidden;
    box-shadow: 0 0 0 1px rgba(60, 45, 10, 0.5);
  }
  .card--front { left: 18px; }
  .card--back { left: 619px; }

  .front-band {
    position: absolute;
    left: 0;
    top: 93px;
    width: 100%;
    height: 160px;
    background: var(--mist);
  }
  .brand {
    position: absolute;
    left: 0;
    top: 0;
    width: 100%;
    height: 100%;
    display: flex;
    flex-direction: column;
    align-items: center;
    justify-content: center;
    gap: 12px;
  }
  .brand-seal {
    width: 48px;
    height: 48px;
    border-radius: 50%;
    background: var(--bark);
  }
  .brand-name {
    font-family: "Arimo", sans-serif;
    font-weight: 400;
    font-size: 32px;
    color: var(--bark);
    letter-spacing: 0.5px;
  }

  .back-seal {
    position: absolute;
    left: 40px;
    top: 80px;
    width: 150px;
    height: 150px;
    border-radius: 50%;
    background: var(--seal);
  }
  .holder-name {
    position: absolute;
    left: 241px;
    top: 84px;
    margin: 0;
    font-family: "Arimo", sans-serif;
    font-weight: 700;
    font-style: italic;
    font-size: 25px;
    color: var(--ink-white);
  }
  .contact-list {
    position: absolute;
    left: 241px;
    top: 130px;
    margin: 0;
    padding: 0;
    list-style: none;
    font-family: "Arimo", sans-serif;
    font-size: 16px;
    color: var(--ink-white);
  }
  .contact-item {
    display: flex;
    align-items: center;
    height: 26px;
  }
  .contact-item--web { margin-top: 3px; }
  .contact-icon {
    width: 16px;
    height: 16px;
    margin-right: 6px;
    fill: var(--ink-white);
  }
  .address-band {
    position: absolute;
    left: 0;
    bottom: 0;
    width: 100%;
    height: 39px;
    background: var(--mist);
    display: flex;
    align-items: center;
    justify-content: center;
    font-family: "Arimo", sans-serif;
    font-size: 16px;
    color: var(--bark);
  }
</style>
</head>
<body>
<div class="canvas">
  <div class="side-label side-label--front">FRONT</div>
  <div class="side-label side-label--back">BACK</div>

  <section class="card card--front">
    <div class="front-band">
      <div class="brand">
        <div class="brand-seal"></div>
        <div class="brand-name">Crestview Property Walk</div>
      </div>
    </div>
  </section>

  <section class="card card--back">
    <div class="back-seal"></div>
    <h2 class="holder-name">Derek Osmund</h2>
    <ul class="contact-list">
      <li class="contact-item">
        <svg class="contact-icon" viewBox="0 0 16 16" aria-label="Office">
          <rect x="1" y="3" width="3" height="11" rx="1"/>
          <rect x="5" y="3" width="10" height="11" rx="1"/>
          <rect x="7" y="5" width="6" height="2" fill="#5c4a1e"/>
          <rect x="7" y="9" width="6" height="3" fill="#5c4a1e"/>
        </svg>
        <span>: 626.748.1196</span>
      </li>
      <li class="contact-item">
        <svg class="contact-icon" viewBox="0 0 16 16" aria-label="Mobile">
          <rect x="5" y="2" width="7" height="12" rx="1"/>
          <rect x="6.3" y="3.5" width="4.4" height="5" fill="#5c4a1e"/>
        </svg>
        <span>: 626.913.4071</span>
      </li>
      <li class="contact-item">
        <svg class="contact-icon" viewBox="0 0 16 16" aria-label="Email">
          <rect x="2" y="4.5" width="12" height="8"/>
          <path d="M2 4.5 L8 9 L14 4.5" fill="none" stroke="#5c4a1e" stroke-width="1.2"/>
        </svg>
        <span>: Derek@CrestviewPropertyWalk.example</span>
      </li>
      <li class="contact-item contact-item--web">
        <svg class="contact-icon" viewBox="0 0 16 16" aria-label="Web">
          <circle cx="8" cy="8" r="6"/>
          <path d="M2 8 H14 M8 2 V14 M8 2 C5 5 5 11 8 14 M8 2 C11 5 11 11 8 14" fill="none" stroke="#5c4a1e" stroke-width="1"/>
        </svg>
        <span>: www.CrestviewPropertyWalk.example</span>
      </li>
    </ul>
    <div class="address-band">482 W. Fenwick St., Suite 310, Pasadena, CA 91348</div>
  </section>
</div>
</body>
</html>
```